****Business Card Design for Cormorant Ridge. Design based around attached logo/company name

I’m looking for business card design for my company Cormorant Ridge Holdings,LLC. Design should be professional, sharp and minimal. Outside of the attached logos, greyscale colors for remainder of cards. My thoughts are two-sided card with attached logo on one side and my info on the other but open to one-sided as well with right design.
Target Market(s)
Real estate professionals including banks, private investors, property owners, developers, commercial tenants like Brewloft, Grocana or Tandberry’s.
Industry/Entity Type
Commercial real estate development and investments.
Contact Information for Business Card
Name, title, email, phone #’s, web address and physical address
Font styles to use
Other font styles liked:
- Helvetica, Garamond, etc
Colors
Designer to choose only greyscale colors for use in the design.
Requirements
Must have
- Attached logo first or second options.
Nice to have
- Two sided card with logo on one side. Attached Logo/company name can be laid out any way that flows as long as it’s legible.name
Should not have
- No loud colors. ***Please do not include logo, I have removed the company design with a logo image.

```html
<!DOCTYPE html>
<html lang="en">
<head>
<meta charset="UTF-8">
<title>Cormorant Ridge Holdings – Business Card</title>
<link href="https://fonts.googleapis.com/css2?family=EB+Garamond:ital,wght@0,400;1,400&display=swap" rel="stylesheet">
<style>
  :root {
    --backdrop: #cbcbcb;
    --card: #435d7a;
    --ink-soft: #c3c7cc;
    --ink-bright: #ffffff;
  }
  * { margin: 0; padding: 0; box-sizing: border-box; }
  html, body {
    width: 1200px;
    height: 846px;
    overflow: hidden;
    background: var(--backdrop);
  }
  .canvas {
    position: relative;
    width: 1200px;
    height: 846px;
    font-family: "EB Garamond", Garamond, serif;
  }
  .card {
    position: absolute;
    left: 346px;
    width: 508px;
    height: 290px;
    background: var(--card);
  }
  .card--front { top: 115px; }
  .card--back { top: 445px; }

  .contact {
    position: absolute;
    left: 110px;
    top: 38px;
    color: var(--ink-soft);
  }
  .contact__name {
    margin-left: 28px;
    font-size: 23px;
    line-height: 26px;
    font-weight: 400;
  }
  .contact__title {
    margin-left: 28px;
    font-size: 20px;
    line-height: 24px;
    font-style: italic;
  }
  .contact__list {
    list-style: none;
    margin-top: 22px;
  }
  .contact__item {
    display: flex;
    align-items: center;
    font-size: 19px;
    line-height: 24px;
  }
  .contact__item--address {
    margin-top: 20px;
    align-items: center;
    line-height: 20px;
  }
  .contact__icon {
    width: 18px;
    height: 18px;
    margin-right: 10px;
    flex: none;
  }
  .contact__icon--pin { width: 18px; height: 26px; }

  .brand {
    position: absolute;
    inset: 0;
    display: flex;
    flex-direction: column;
    justify-content: center;
    align-items: center;
    color: var(--ink-bright);
    font-size: 30px;
    line-height: 36px;
    letter-spacing: 0.12em;
    text-transform: uppercase;
    text-align: center;
  }
</style>
</head>
<body>
<main class="canvas">
  <section class="card card--front" aria-label="Card front – contact details">
    <div class="contact">
      <h1 class="contact__name">Daniel Hartwell</h1>
      <p class="contact__title">Title</p>
      <ul class="contact__list">
        <li class="contact__item">
          <svg class="contact__icon" viewBox="0 0 24 24" fill="none" stroke="currentColor" stroke-width="1.8" stroke-linecap="round" stroke-linejoin="round"><path d="M6 3l3 4-2 2c1 3 3 5 6 6l2-2 4 3-2 4C10 20 4 14 3 6z"/><path d="M14 4a6 6 0 0 1 6 6"/><path d="M14 7.5a2.5 2.5 0 0 1 2.5 2.5"/></svg>
          404-555-0172
        </li>
        <li class="contact__item">
          <svg class="contact__icon" viewBox="0 0 24 24"><rect x="2" y="6" width="20" height="13" fill="currentColor"/><path d="M2 6l10 7 10-7M2 19l8-6M22 19l-8-6" fill="none" stroke="#435d7a" stroke-width="1.4"/></svg>
          danielhartwell@cormorantridge.com
        </li>
        <li class="contact__item">
          <svg class="contact__icon" viewBox="0 0 24 24" fill="none" stroke="currentColor" stroke-width="1.5"><circle cx="12" cy="12" r="9.5"/><ellipse cx="12" cy="12" rx="4.2" ry="9.5"/><path d="M2.5 12h19M4 7h16M4 17h16"/></svg>
          www.cormorantridge.com
        </li>
        <li class="contact__item contact__item--address">
          <svg class="contact__icon contact__icon--pin" viewBox="0 0 18 26"><path d="M9 1a8 8 0 0 0-8 8c0 6 8 16 8 16s8-10 8-16a8 8 0 0 0-8-8z" fill="currentColor"/><circle cx="9" cy="9" r="3.2" fill="#435d7a"/></svg>
          <span>1840 Larkspur Lane Ne<br>Atlanta, GA 30309</span>
        </li>
      </ul>
    </div>
  </section>

  <section class="card card--back" aria-label="Card back – company name">
    <p class="brand">Cormorant Ridge<br>Holdings, LLC</p>
  </section>
</main>
</body>
</html>
```